VENTURE CAPITAL GROUP BUSINESS CARD DESIGN

Venture Capital Group based in SF looking for a bold business card design. No trendy colour explosion, 3D effects etc. Just "simple" optical effects. Works on your brain, keeps your eye focused and sticks to your mind.
Target Market(s)
Technology startups
Industry/Entity Type
Venture Capital
Contact Information for Business Card
BARTHOLOMEW ELLING
MANAGING PARTNER
817 FERN ST SAN FRANCISCO, CA 94111
415.555.0142 O
415.555.0187 F
415.555.0236 C
bart@quillbrookfunds.example

```html
<!DOCTYPE html>
<html lang="en">
<head>
<meta charset="utf-8">
<title>Quillbrook Capital Group – Business Card</title>
<link rel="stylesheet" href="https://fonts.googleapis.com/css2?family=Cinzel:wght@500&family=Quattrocento:wght@400&family=Saira+Semi+Condensed:wght@600&display=swap">
<style>
  :root {
    --backdrop: #a5a3a4;
    --paper: #fdfdfd;
    --green: #1f8a3a;
    --green-dark: #116634;
    --green-light: #5cc05a;
    --grey-text: #555555;
    --grey-rule: #9a9a9a;
    --white: #ffffff;
  }
  * { margin: 0; padding: 0; box-sizing: border-box; }
  html, body { width: 1200px; height: 1200px; overflow: hidden; }
  body { background: var(--backdrop); position: relative; font-family: "Quattrocento", serif; }

  .card {
    position: absolute;
    width: 715px;
    height: 418px;
    background: var(--paper);
    overflow: hidden;
  }
  .card--front { left: 238px; top: 118px; }
  .card--back  { left: 229px; top: 644px; }

  .card__art { position: absolute; inset: 0; }

  /* Front */
  .front-brand {
    position: absolute;
    left: 0; right: 0; top: 90px;
    display: flex; flex-direction: column; align-items: center;
    color: var(--green);
    font-family: "Cinzel", serif;
    font-weight: 500;
  }
  .brand-dot {
    width: 150px; height: 150px; border-radius: 50%;
    background: #eeeeee;
    margin-bottom: 22px;
  }
  .front-brand .brand-name { font-size: 44px; line-height: 1; letter-spacing: 1px; }
  .front-brand .brand-sub { font-size: 14px; letter-spacing: 7px; margin-top: 6px; }

  /* Back */
  .holder {
    position: absolute; right: 30px; top: 48px;
    text-align: right; color: var(--white);
  }
  .holder__name {
    font-family: "Saira Semi Condensed", sans-serif;
    font-weight: 600; font-size: 26px; line-height: 1.1;
  }
  .holder__title { font-family: "Quattrocento", serif; font-size: 17px; margin-top: 4px; }

  .back-brand {
    position: absolute; left: 48px; top: 142px;
    display: flex; align-items: center; gap: 30px;
    color: var(--green);
    font-family: "Cinzel", serif; font-weight: 500;
  }
  .back-brand .brand-dot { width: 86px; height: 86px; margin: 0; }
  .back-brand .brand-name { font-size: 40px; line-height: 1; letter-spacing: 1px; }
  .back-brand .brand-sub { font-size: 13px; letter-spacing: 6px; margin-top: 4px; padding-left: 70px; }

  .contact {
    position: absolute; top: 290px;
    list-style: none;
    color: var(--grey-text);
    font-size: 18px;
  }
  .contact--phones { left: 36px; }
  .contact--web { left: 250px; }
  .contact li { display: flex; align-items: center; height: 26px; gap: 12px; }
  .contact svg { width: 18px; height: 18px; flex: none; fill: var(--green-dark); }
</style>
</head>
<body>

  <section class="card card--front" aria-label="Card front">
    <div class="front-brand">
      <div class="brand-dot"></div>
      <div class="brand-name">Quillbrook</div>
      <div class="brand-sub">Capital Group</div>
    </div>
  </section>

  <section class="card card--back" aria-label="Card back">
    <svg class="card__art" viewBox="0 0 715 418" preserveAspectRatio="none" aria-hidden="true">
      <defs>
        <linearGradient id="bandGreen" x1="0" y1="0" x2="1" y2="0">
          <stop offset="0" stop-color="#5cc05a"/>
          <stop offset="0.55" stop-color="#1f8a3a"/>
          <stop offset="1" stop-color="#116634"/>
        </linearGradient>
        <linearGradient id="swooshGrey" x1="0" y1="0" x2="1" y2="0">
          <stop offset="0" stop-color="#d8d8d8"/>
          <stop offset="0.5" stop-color="#8e8e8e"/>
          <stop offset="1" stop-color="#b5b5b5"/>
        </linearGradient>
      </defs>
      <path class="band" d="M0 0 H715 V168 C600 172 520 140 440 100 C340 50 220 20 0 40 Z" fill="url(#bandGreen)"/>
      <path class="swoosh" d="M0 62 C180 20 320 40 430 110 C520 165 600 190 715 192 V210 C600 205 510 185 420 130 C320 70 170 50 0 92 Z" fill="url(#swooshGrey)"/>
      <path d="M0 45 C200 15 330 30 440 100 C530 155 620 178 715 180 V192 C610 190 530 165 430 110 C320 40 180 20 0 62 Z" fill="#ffffff"/>
    </svg>

    <div class="holder">
      <div class="holder__name">Bartholomew Elling</div>
      <div class="holder__title">Managing Partner</div>
    </div>

    <div class="back-brand">
      <div class="brand-dot"></div>
      <div>
        <div class="brand-name">Quillbrook</div>
        <div class="brand-sub">Capital Group</div>
      </div>
    </div>

    <ul class="contact contact--phones">
      <li>
        <svg viewBox="0 0 24 24" aria-label="Office"><path d="M3 8c0-2 4-4 9-4s9 2 9 4v2h-5V8H8v2H3z M6 11h12l2 9H4z"/></svg>
        415.555.0142
      </li>
      <li>
        <svg viewBox="0 0 24 24" aria-label="Fax"><path d="M7 3h10v5H7z M4 9h16v8h-3v4H7v-4H4z M9 15v4h6v-4z"/></svg>
        415.555.0187
      </li>
      <li>
        <svg viewBox="0 0 24 24" aria-label="Mobile"><path d="M7 2h10a1 1 0 0 1 1 1v18a1 1 0 0 1-1 1H7a1 1 0 0 1-1-1V3a1 1 0 0 1 1-1z M8 4v14h8V4z M11 19h2v2h-2z"/></svg>
        415.555.0236
      </li>
    </ul>

    <ul class="contact contact--web">
      <li>
        <svg viewBox="0 0 24 24" aria-label="Email"><path d="M2 5h20v14H2z M4 7v.5l8 6 8-6V7l-8 6z" fill-rule="evenodd"/></svg>
        bart@quillbrookfunds.example
      </li>
      <li>
        <svg viewBox="0 0 24 24" aria-label="Website"><path d="M12 2a10 10 0 1 0 0 20 10 10 0 0 0 0-20zm-1 2.1V8H7.4A8 8 0 0 1 11 4.1zm2 0A8 8 0 0 1 16.6 8H13zM5.3 10H11v4H5.3a8 8 0 0 1 0-4zm7.7 0h5.7a8 8 0 0 1 0 4H13zM7.4 16H11v3.9A8 8 0 0 1 7.4 16zm5.6 0h3.6A8 8 0 0 1 13 19.9z"/></svg>
        www.quillbrookfunds.example
      </li>
      <li>
        <svg viewBox="0 0 24 24" aria-label="Address"><path d="M12 2a7 7 0 0 0-7 7c0 5 7 13 7 13s7-8 7-13a7 7 0 0 0-7-7zm0 4a3 3 0 1 1 0 6 3 3 0 0 1 0-6z"/></svg>
        817 Fern St San Francisco, CA 94111
      </li>
    </ul>
  </section>

</body>
</html>
```